I want a double sided flyer possibly with a picture of a lawn or grass.
Company name, phone number, email, and logo
Halvorsen Turf Management, (404)726-1853,Halvorsen_Turf@brevimail.com
Company services
Fertilization and weed control,Lawn and Landscape maintenance, mowing, pruning, aeration, landscape and Christmas lights,

```html
<!DOCTYPE html>
<html lang="en">
<head>
<meta charset="utf-8">
<title>Halvorsen Turf Management</title>
<link rel="stylesheet" href="https://fonts.googleapis.com/css2?family=Oswald:wght@700&family=PT+Sans:ital,wght@0,400;0,700;1,700&display=swap">
<style>
:root{
  --sky-top:#1f7fd4;
  --sky-mid:#5fb2ec;
  --sky-low:#cfe9fb;
  --grass-light:#b6e34a;
  --grass-deep:#4f9a12;
  --lime:#c4ec1c;
  --lime-dark:#7fb10a;
  --ink:#111;
  --white:#fff;
  --title-outline:#0d4f8c;
  --leaf:#3f9c2a;
}
*{margin:0;padding:0;box-sizing:border-box}
html,body{width:1200px;height:566px;overflow:hidden;background:#fff}
.flyer{position:relative;width:1200px;height:566px;overflow:hidden;font-family:"PT Sans",Arial,sans-serif;color:var(--ink)}
.scenery{position:absolute;inset:0;
  background:
    radial-gradient(ellipse 230px 330px at 1080px 300px,rgba(255,255,255,.85),rgba(255,240,245,.45) 60%,rgba(255,255,255,0) 100%),
    linear-gradient(180deg,rgba(0,0,0,0) 0 405px,var(--grass-light) 420px,#8fcf2a 470px,var(--grass-deep) 566px),
    linear-gradient(180deg,var(--sky-top) 0,var(--sky-mid) 150px,var(--sky-low) 400px);}
.side-panel{position:absolute;left:45px;top:0;width:328px;height:566px;
  background:linear-gradient(90deg,var(--lime-dark),var(--lime) 40%,var(--lime) 70%,var(--lime-dark));
  box-shadow:-6px 0 10px rgba(0,0,0,.45),6px 0 10px rgba(0,0,0,.45);}
.tagline-badge{position:absolute;left:28px;top:-10px}
.tagline{position:absolute;left:50px;top:28px;width:340px;text-align:center;color:var(--white);
  font-style:italic;font-weight:700;font-size:29px;line-height:40px;text-shadow:1px 1px 2px rgba(0,0,0,.35)}
.brand-mark{position:absolute;left:174px;top:318px;width:70px;height:70px;border-radius:50%;background:var(--ink)}
.brand-name{position:absolute;left:45px;top:400px;width:328px;text-align:center;font-weight:700;font-size:24px;line-height:28px;color:var(--ink)}
.phone{position:absolute;left:45px;top:499px;width:328px;text-align:center;font-weight:700;font-size:29px}
.title{position:absolute;left:446px;top:20px;font-family:"Oswald",Impact,sans-serif;font-weight:700;font-size:84px;line-height:104px;
  color:var(--lime);letter-spacing:1px;transform:scaleX(.76);transform-origin:left top;white-space:nowrap;
  -webkit-text-stroke:3px var(--title-outline);paint-order:stroke fill;
  text-shadow:0 0 8px var(--white),0 0 14px var(--white)}
.title-sub{position:absolute;left:791px;top:74px;font-style:italic;font-weight:700;font-size:23px}
.services-bar{position:absolute;left:488px;top:146px;width:300px;height:36px;
  background:linear-gradient(90deg,rgba(0,0,0,0),#000 18%,#000 75%,rgba(0,0,0,0));
  color:var(--white);font-style:italic;font-weight:700;font-size:25px;line-height:36px;padding-left:85px}
.intro{position:absolute;left:503px;top:198px;font-size:19px}
.service-list{position:absolute;left:502px;top:232px;list-style:none}
.service-list li{display:flex;align-items:center;height:22px;font-weight:700;font-size:17.5px}
.service-list svg{width:24px;height:14px;margin-right:12px}
.email{position:absolute;left:762px;top:528px;font-weight:700;font-size:18px}
</style>
</head>
<body>
<div class="flyer">
  <div class="scenery" role="img" aria-label="Rolling green lawn with a path leading to a house under a blue sky, white blossom branch on the right"></div>

  <div class="side-panel"></div>
  <svg class="tagline-badge" width="360" height="290" viewBox="0 0 360 290">
    <polygon points="180,-90 358,98 180,278 2,98" fill="#7eb20c" stroke="#d8f46a" stroke-width="3"/>
  </svg>
  <p class="tagline">Professional<br>lawn Management<br>at an affordable<br>price</p>

  <div class="brand-mark"></div>
  <p class="brand-name">Halvorsen<br>Turf Management</p>
  <p class="phone">Ph: (404)726-1853</p>

  <h1 class="title">HALVORSEN</h1>
  <p class="title-sub">Turf Management</p>

  <h2 class="services-bar">Services</h2>
  <p class="intro">We specialise in the following services;</p>
  <ul class="service-list">
    <li><svg viewBox="0 0 24 14"><ellipse cx="12" cy="7" rx="11" ry="6" fill="var(--leaf)"/></svg>Fertilization</li>
    <li><svg viewBox="0 0 24 14"><ellipse cx="12" cy="7" rx="11" ry="6" fill="var(--leaf)"/></svg>Weed control</li>
    <li><svg viewBox="0 0 24 14"><ellipse cx="12" cy="7" rx="11" ry="6" fill="var(--leaf)"/></svg>Lawn and Landscape maintenance</li>
    <li><svg viewBox="0 0 24 14"><ellipse cx="12" cy="7" rx="11" ry="6" fill="var(--leaf)"/></svg>Mowing</li>
    <li><svg viewBox="0 0 24 14"><ellipse cx="12" cy="7" rx="11" ry="6" fill="var(--leaf)"/></svg>Pruning</li>
    <li><svg viewBox="0 0 24 14"><ellipse cx="12" cy="7" rx="11" ry="6" fill="var(--leaf)"/></svg>Aeration</li>
    <li><svg viewBox="0 0 24 14"><ellipse cx="12" cy="7" rx="11" ry="6" fill="var(--leaf)"/></svg>Landscape and Christmas lights</li>
    <li><svg viewBox="0 0 24 14"><ellipse cx="12" cy="7" rx="11" ry="6" fill="var(--leaf)"/></svg>Lawn care and advice</li>
  </ul>

  <p class="email">Halvorsen_Turf@brevimail.com</p>
</div>
</body>
</html>
```